Harbor Crest Renewal Business Cards

We need a sleek and sexy business card design

Contact Information for Business Card

Name, address, phone number, email. Vincent Morrasco 482 Pellham Street Suite 200C Holtsville NY 11958 (631)555-0174 Also a second version with the name Derek Halvorn

```html
<!DOCTYPE html>
<html lang="en">
<head>
<meta charset="utf-8">
<title>Harbor Crest Renewal — Business Cards</title>
<link href="https://fonts.googleapis.com/css2?family=Montserrat:wght@400;500;600;700&display=swap" rel="stylesheet">
<style>
  :root {
    --brand-red: #cf4127;
    --brand-navy: #213b8c;
    --ink: #1f1f1f;
    --paper: #ffffff;
    --backdrop: #d2d5d7;
  }
  * { box-sizing: border-box; margin: 0; padding: 0; }
  html, body { width: 1200px; height: 928px; overflow: hidden; }
  body {
    background: var(--backdrop);
    font-family: "Montserrat", sans-serif;
    position: relative;
  }
  .card {
    position: absolute;
    width: 676px;
    height: 386px;
    transform: scale(0.68);
    transform-origin: top left;
  }
  .card--front {
    left: 370px; top: 170px;
    background: var(--brand-red);
    display: flex; flex-direction: column; align-items: center; justify-content: center;
    color: var(--paper);
  }
  .front-mark {
    width: 46px; height: 46px;
    background: var(--paper);
    margin-bottom: 22px;
  }
  .front-name {
    font-weight: 600;
    font-size: 44px;
    line-height: 1;
    letter-spacing: 0.5px;
    text-align: center;
  }
  .card--back {
    top: 476px;
    background: var(--paper);
    overflow: hidden;
  }
  .card--vincent { left: 120px; }
  .card--derek { left: 620px; }
  .back-brand {
    position: absolute;
    left: 40px; top: 130px;
    width: 255px;
    display: flex; flex-direction: column; align-items: center;
    color: var(--brand-navy);
    font-weight: 600;
  }
  .back-brand__mark {
    width: 30px; height: 30px;
    background: var(--brand-navy);
    margin-bottom: 14px;
  }
  .back-brand__name {
    font-size: 30px; line-height: 1.1; text-align: center;
  }
  .accent-bar {
    position: absolute;
    left: 337px; top: 85px;
    width: 4px; height: 44px;
    background: var(--brand-red);
  }
  .divider-line {
    position: absolute;
    left: 338px; top: 142px;
    width: 2px; height: 160px;
    background: var(--brand-navy);
  }
  .person {
    position: absolute; left: 362px; top: 82px;
  }
  .person__name {
    font-weight: 700; font-size: 24px; line-height: 1.2;
    color: var(--brand-navy);
    white-space: nowrap;
  }
  .person__name .surname { color: var(--brand-red); }
  .person__title {
    font-size: 15.5px; font-weight: 500; color: var(--ink);
    margin-top: 4px;
  }
  .address {
    position: absolute; left: 363px; top: 137px;
    width: 165px;
    border-top: 1.5px solid var(--brand-navy);
    border-bottom: 1.5px solid var(--brand-navy);
    padding: 6px 0 4px;
    font-size: 15.5px; font-weight: 500; line-height: 24px; color: var(--ink);
    white-space: nowrap;
  }
  .contact-list {
    position: absolute; left: 365px; top: 227px;
    list-style: none;
  }
  .contact-list li {
    display: flex; align-items: center;
    height: 29.5px;
    font-size: 15.5px; font-weight: 500; color: var(--ink);
    letter-spacing: 0.3px;
    white-space: nowrap;
  }
  .contact-list svg { width: 12px; height: 12px; margin-right: 9px; flex: none; }
  .footer-band {
    position: absolute; left: 0; bottom: 0;
    width: 100%; height: 14px;
    display: flex;
  }
  .footer-band__red { width: 338px; background: var(--brand-red); }
  .footer-band__gap { width: 3px; background: var(--paper); }
  .footer-band__navy { flex: 1; background: var(--brand-navy); }
</style>
</head>
<body>

<section class="card card--front">
  <div class="front-mark"></div>
  <div class="front-name">Harbor Crest Renewal</div>
</section>

<section class="card card--back card--vincent">
  <div class="back-brand">
    <div class="back-brand__mark"></div>
    <div class="back-brand__name">Harbor Crest Renewal</div>
  </div>
  <div class="accent-bar"></div>
  <div class="divider-line"></div>
  <div class="person">
    <div class="person__name">Vincent <span class="surname">Morrasco</span></div>
    <div class="person__title">Director</div>
  </div>
  <div class="address">
    482 Pellham Street<br>
    Suite 200C<br>
    Holtsville NY 11958
  </div>
  <ul class="contact-list">
    <li>
      <svg viewBox="0 0 12 12" aria-hidden="true"><path d="M2.5 1 L4.5 1 L5.3 3.4 L4 4.4 C4.7 6 6 7.3 7.6 8 L8.6 6.7 L11 7.5 L11 9.5 C11 10.3 10.3 11 9.5 11 C5 11 1 7 1 2.5 C1 1.7 1.7 1 2.5 1 Z" fill="none" stroke="#cf4127" stroke-width="1.3"/></svg>
      (631)555-0174
    </li>
    <li>
      <svg viewBox="0 0 12 12" aria-hidden="true"><rect x="0.5" y="2" width="11" height="8" fill="#cf4127"/><path d="M0.5 2.5 L6 6.5 L11.5 2.5" fill="none" stroke="#fff" stroke-width="1"/></svg>
      info@harborcrestrenewal.com
    </li>
    <li>
      <svg viewBox="0 0 12 12" aria-hidden="true"><g fill="none" stroke="#cf4127" stroke-width="1"><circle cx="6" cy="6" r="5.2"/><ellipse cx="6" cy="6" rx="2.3" ry="5.2"/><line x1="0.8" y1="6" x2="11.2" y2="6"/><line x1="1.6" y1="3.3" x2="10.4" y2="3.3"/><line x1="1.6" y1="8.7" x2="10.4" y2="8.7"/></g></svg>
      www.harborcrestrenewal.com
    </li>
  </ul>
  <div class="footer-band">
    <div class="footer-band__red"></div>
    <div class="footer-band__gap"></div>
    <div class="footer-band__navy"></div>
  </div>
</section>

<section class="card card--back card--derek">
  <div class="back-brand">
    <div class="back-brand__mark"></div>
    <div class="back-brand__name">Harbor Crest Renewal</div>
  </div>
  <div class="accent-bar"></div>
  <div class="divider-line"></div>
  <div class="person">
    <div class="person__name">Derek <span class="surname">Halvorn</span></div>
    <div class="person__title">Director</div>
  </div>
  <div class="address">
    482 Pellham Street<br>
    Suite 200C<br>
    Holtsville NY 11958
  </div>
  <ul class="contact-list">
    <li>
      <svg viewBox="0 0 12 12" aria-hidden="true"><path d="M2.5 1 L4.5 1 L5.3 3.4 L4 4.4 C4.7 6 6 7.3 7.6 8 L8.6 6.7 L11 7.5 L11 9.5 C11 10.3 10.3 11 9.5 11 C5 11 1 7 1 2.5 C1 1.7 1.7 1 2.5 1 Z" fill="none" stroke="#cf4127" stroke-width="1.3"/></svg>
      (631)555-0174
    </li>
    <li>
      <svg viewBox="0 0 12 12" aria-hidden="true"><rect x="0.5" y="2" width="11" height="8" fill="#cf4127"/><path d="M0.5 2.5 L6 6.5 L11.5 2.5" fill="none" stroke="#fff" stroke-width="1"/></svg>
      info@harborcrestrenewal.com
    </li>
    <li>
      <svg viewBox="0 0 12 12" aria-hidden="true"><g fill="none" stroke="#cf4127" stroke-width="1"><circle cx="6" cy="6" r="5.2"/><ellipse cx="6" cy="6" rx="2.3" ry="5.2"/><line x1="0.8" y1="6" x2="11.2" y2="6"/><line x1="1.6" y1="3.3" x2="10.4" y2="3.3"/><line x1="1.6" y1="8.7" x2="10.4" y2="8.7"/></g></svg>
      www.harborcrestrenewal.com
    </li>
  </ul>
  <div class="footer-band">
    <div class="footer-band__red"></div>
    <div class="footer-band__gap"></div>
    <div class="footer-band__navy"></div>
  </div>
</section>

</body>
</html>
```